Poster design for the WILLOW WISP magic show.

We need a poster design for our magic show. This isn't your typical 'small town' magic show. Our show features world class magicians from the Velvet Lantern, in Hollywood California. The show is geared toward everyone, it is family friendly - with a little bit of an edge. We want people to see the poster and feel like they are going to have a unique and sophisticated magical experience. We also want individuals and couples to see the poster and feel like it is a show for them and not only for children.
Updates

Target Market(s)

BRT audience, family audience, the age range is anywhere from 5 - 105. Cool people.

Industry/Entity Type

Town

Requirements
Must have
• Our attached .jpg of the magician floating in the air. Poster size 24x36"
Must have text:
The 3rd Annual Albuquerque Conjuring Gala Presents (small type)
Willow Wisp (should be larger type)
November 24th - 25th
Showtimes 3:00PM & 7:30PM Saturday, 2:00PM Sunday
Tickets available at www.DorvaSeats.example For more information contact Dorva Theatre @ 505.555.0147
Nice to have
• A sort of old school/antique feeling to the poster.
Perhaps a theater marquee
Check out www.grovelumen.example - we love the feeling of this site for our poster...
Feel free to adjust the provided .jpg accordingly in regards to color/size/interaction with the rest of the poster
Should not have
• Should not have clowns, bunnies, anything that would make it feel like a 3 year old's magic themed birthday party.

```html
<!DOCTYPE html>
<html lang="en">
<head>
<meta charset="utf-8">
<title>Willow Wisp — Poster</title>
<link rel="stylesheet" href="https://fonts.googleapis.com/css2?family=Didact+Gothic&family=Poiret+One&display=swap">
<style>
  :root {
    --ink: #000000;
    --gold: #c9a227;
    --gold-soft: #b8922a;
    --band-light: #c99a2c;
    --band-dark: #9a6a1c;
    --text-dark: #0d0a05;
    --photo-light: #8a8580;
    --photo-dark: #1e1c1a;
  }
  html, body {
    margin: 0;
    padding: 0;
    width: 800px;
    height: 1200px;
    overflow: hidden;
    background: #ffffff;
  }
  .poster {
    position: relative;
    width: 800px;
    height: 1200px;
    background: var(--ink);
    font-family: "Didact Gothic", "Century Gothic", sans-serif;
    color: var(--gold);
    text-align: center;
    overflow: hidden;
  }
  .poster__inner {
    position: absolute;
    left: 22px; top: 22px; right: 22px; bottom: 24px;
    background: var(--ink);
    overflow: hidden;
  }
  .poster__band {
    position: absolute;
    left: 0; right: 0; top: 775px; bottom: 0;
    background:
      radial-gradient(ellipse at 20% 40%, rgba(230,180,60,.55), transparent 60%),
      radial-gradient(ellipse at 95% 90%, rgba(140,80,30,.7), transparent 55%),
      linear-gradient(180deg, var(--band-light) 0%, var(--gold-soft) 60%, var(--band-dark) 100%);
  }
  .poster__rule {
    position: absolute;
    left: 28px; top: 28px; right: 28px; bottom: 30px;
    border: 2px solid var(--gold);
    pointer-events: none;
  }
  .line { position: absolute; left: 0; right: 0; margin: 0; font-weight: 400; }
  .presenter { top: 54px; font-size: 24px; letter-spacing: 2px; }
  .presents { top: 102px; font-size: 20px; letter-spacing: 2px; }
  .title {
    top: 128px;
    font-family: "Poiret One", "Didact Gothic", sans-serif;
    font-size: 118px;
    font-variant: small-caps;
    letter-spacing: 6px;
    line-height: 1.1;
  }
  .dates { top: 270px; font-size: 32px; letter-spacing: 3px; }
  .showtimes-label { top: 343px; font-size: 20px; letter-spacing: 2px; }
  .showtime { font-size: 33px; letter-spacing: 2px; }
  .showtime--sat { top: 370px; }
  .showtime--sun { top: 412px; }
  .marquee {
    position: absolute;
    left: 62px; top: 480px;
    width: 680px; height: 510px;
  }
  .marquee__photo {
    position: absolute;
    left: 142px; top: 45px;
    width: 396px; height: 390px;
    background: radial-gradient(ellipse at 55% 40%, var(--photo-light) 0%, #4d4946 50%, var(--photo-dark) 100%);
    border-radius: 40px;
  }
  .tickets { color: var(--text-dark); }
  .tickets__lead { top: 1010px; font-size: 30px; letter-spacing: 3px; }
  .tickets__url { top: 1046px; font-size: 30px; letter-spacing: 2px; }
  .tickets__info { top: 1082px; font-size: 22px; letter-spacing: 1.5px; }
  .tickets__phone { top: 1110px; font-size: 22px; letter-spacing: 1.5px; }
</style>
</head>
<body>
  <main class="poster">
    <div class="poster__inner">
      <div class="poster__band"></div>
    </div>
    <div class="poster__rule"></div>

    <p class="line presenter">The 3rd Annual Albuquerque Conjuring Gala</p>
    <p class="line presents">PRESENTS</p>
    <h1 class="line title">Willow Wisp</h1>
    <p class="line dates">November 24th - 25th</p>
    <p class="line showtimes-label">SHOWTIMES</p>
    <p class="line showtime showtime--sat">3:00PM &amp; 7:30PM Saturday</p>
    <p class="line showtime showtime--sun">2:00PM Sunday</p>

    <div class="marquee">
      <svg class="marquee__frame" width="680" height="510" viewBox="0 0 680 510" aria-hidden="true">
        <rect x="6" y="6" width="668" height="498" rx="70" fill="#000" stroke="var(--gold)" stroke-width="2"/>
        <rect x="30" y="30" width="620" height="450" rx="56" fill="none" stroke="var(--gold)" stroke-width="2"/>
        <g fill="#e8b93a">
          <circle cx="18" cy="255" r="5"/><circle cx="662" cy="255" r="5"/>
          <circle cx="340" cy="18" r="5"/><circle cx="340" cy="492" r="5"/>
        </g>
      </svg>
      <div class="marquee__photo" role="img" aria-label="Photo of the magician leaning back on stage, holding a floating yellow chair"></div>
    </div>

    <p class="line tickets tickets__lead">Tickets available at</p>
    <p class="line tickets tickets__url">www.DorvaSeats.example</p>
    <p class="line tickets tickets__info">For more information contact</p>
    <p class="line tickets tickets__phone">Dorva Theatre:&nbsp; 505.555.0147</p>
  </main>
</body>
</html>
```